Quarrytide Hosting - Direct Mailer / Flyer

We are excited to announce the launch of our new company, Quarrytide Hosting, a premier cohosting facility and data center dedicated to Cryptocurrency Miners. Our website, https://quarrytidehosting.example, provides detailed information about our offerings and showcases the innovative design schemes for the entire project.

Quarrytide Hosting stands out in the industry by offering both GPU Hosting and ASIC Hosting services in our state-of-the-art facility, equipped with an impressive 17 Megawatts of available power. What sets us apart is our unique billing system based on actual metered power usage. We charge $0.08 for ASIC miners and $0.09 for GPU miners, ensuring cost-effectiveness and transparency for our clients.

Our commitment to excellence is evident in our use of cutting-edge technology, top-notch facilities, and strategic partnerships. These elements come together to deliver exceptional solutions tailored for real-world applications in the cryptocurrency space.

As part of our promotional efforts, we are developing a direct mailer/flyer to introduce Quarrytide Hosting to a wider audience. This promotional material will also serve as a handout at events, to potential customers, and more. We welcome creative ideas and suggestions to maximize the versatility of this design and reach diverse target audiences effectively.

For a comprehensive overview of our services and to explore our design concepts, please visit https://quarrytidehosting.example. Quarrytide Hosting is poised to revolutionize the mining industry, and we look forward to partnering with you for success in the digital currency era.

```html
<!DOCTYPE html>
<html lang="en">
<head>
<meta charset="utf-8">
<title>Quarrytide Hosting – Direct Mailer</title>
<link href="https://fonts.googleapis.com/css2?family=Chakra+Petch:wght@600;700&family=Poppins:wght@300;400;500&display=swap" rel="stylesheet">
<style>
  :root{
    --ink:#1d1d1f;
    --muted:#4a4a52;
    --blue:#3d5af1;
    --blue-deep:#2c47ee;
    --green:#1f9d4c;
    --panel-blue:#e8ebf6;
    --panel-green:#e7f0ea;
    --tint:#f2f3f7;
    --bar:#eef0f5;
    --line:#d9dbe2;
    --stage:#ececee;
    --white:#ffffff;
  }
  *{box-sizing:border-box;margin:0;padding:0}
  html,body{width:1200px;height:2218px;overflow:hidden}
  body{background:var(--stage);font-family:"Poppins",sans-serif;color:var(--ink);position:relative}
  .card{position:absolute;left:80px;width:1010px;height:673px;background:var(--white);transform:scale(1.0297);transform-origin:0 0;box-shadow:0 12px 40px rgba(0,0,0,.10);overflow:hidden}
  .card--front{top:376px}
  .card--back{top:1149px}
  .abs{position:absolute}
  .display{font-family:"Chakra Petch",sans-serif;font-weight:700;letter-spacing:-.3px}

  /* front */
  .front__hero{left:0;top:0;width:1010px;height:346px;background:var(--tint)}
  .front__network{left:536px;top:0;width:474px;height:346px;background:radial-gradient(circle at 62% 45%,#cdd6fb 0%,#e4e8fb 40%,var(--tint) 80%)}
  .brand{display:flex;align-items:center;gap:10px;font-family:"Chakra Petch",sans-serif;font-weight:700;color:var(--ink);white-space:nowrap}
  .brand__mark{background:var(--ink)}
  .front__brand{left:55px;top:48px;font-size:34px}
  .front__brand .brand__mark{width:34px;height:34px}
  .front__title{left:55px;top:118px;font-size:49px;line-height:49px}
  .front__lede{left:55px;top:240px;font-size:16px;line-height:18px;width:460px}
  .tag{display:flex;align-items:center;gap:9px;height:42px;padding:0 16px;border-radius:6px;background:rgba(206,216,252,.85);color:var(--blue);font-size:14px;font-weight:500;white-space:nowrap}
  .tag svg{width:18px;height:18px;stroke:var(--blue);fill:none;stroke-width:1.8}
  .offer{left:55px;top:313px;width:247px;height:322px;background:var(--blue);border-radius:6px;color:var(--white);overflow:hidden}
  .offer__copy{padding:16px 16px 0;font-size:12px;line-height:14px;font-weight:300}
  .offer__copy p+p{margin-top:12px}
  .offer__rates{position:absolute;left:0;top:168px;width:100%;height:103px;background:var(--blue-deep);padding:8px 16px 0}
  .offer__lead{font-size:24px;font-weight:300;text-align:center}
  .offer__prices{display:flex;justify-content:space-between;margin-top:2px}
  .price b{display:block;font-family:"Chakra Petch",sans-serif;font-weight:700;font-size:33px;line-height:34px}
  .price span{font-size:12px;font-weight:300}
  .offer__note{position:absolute;left:20px;top:278px;font-size:13px;line-height:15px;font-weight:300}
  .service{top:400px;width:130px}
  .service--wide{width:170px}
  .service__icon{width:48px;height:46px;border-radius:6px;background:linear-gradient(135deg,#cfeedb,#e6f6ec);border:2px solid var(--green)}
  .service__name{font-family:"Chakra Petch",sans-serif;font-weight:700;font-size:16px;margin-top:14px;white-space:nowrap}
  .service__text{font-size:11.5px;line-height:13.5px;color:var(--muted);margin-top:4px}
  .service--wide .service__text{width:140px}
  .divider{top:384px;width:1px;height:176px;background:var(--line)}
  .front__bar{left:302px;top:585px;width:708px;height:54px;background:var(--bar)}
  .contacts{display:flex;align-items:center;white-space:nowrap}
  .contacts span{display:flex;align-items:center;gap:7px}
  .contacts svg{flex:0 0 16px;width:16px;height:16px;fill:none;stroke-width:1.6}
  .front__contacts{left:332px;top:602px;gap:22px;font-size:13.5px;color:var(--ink)}
  .front__contacts svg{stroke:var(--blue)}

  /* back */
  .back__title{left:50px;top:38px;font-size:34px;line-height:37px}
  .back__lede{left:56px;top:128px;font-size:14.5px;line-height:16px;color:var(--muted);width:520px}
  .plan{top:185px;width:252px;height:316px;padding:20px 18px 0}
  .plan--gpu{left:44px;background:var(--panel-blue)}
  .plan--asic{left:308px;background:var(--panel-green)}
  .plan__head{display:flex;gap:22px;align-items:flex-start}
  .plan__icon{width:80px;height:64px;border-radius:6px}
  .plan--gpu .plan__icon{background:linear-gradient(135deg,#c6d0fb,#dfe5fd);border:2px solid var(--blue)}
  .plan--asic .plan__icon{width:70px;background:linear-gradient(135deg,#c7e8d3,#e1f2e7);border:2px solid var(--green)}
  .plan__name{font-family:"Chakra Petch",sans-serif;font-weight:700;font-size:25px;line-height:29px;margin-top:4px}
  .plan--gpu .plan__name{color:var(--blue)}
  .plan--asic .plan__name{color:var(--green)}
  .plan__text{font-size:11.5px;line-height:13.5px;color:var(--muted);margin-top:30px}
  .plan__list{list-style:none;margin-top:18px}
  .plan__list li{display:flex;gap:10px;font-size:11.5px;line-height:13.5px;color:var(--muted);margin-bottom:14px}
  .plan__list svg{flex:0 0 14px;width:14px;height:14px;margin-top:1px}
  .back__band{left:0;top:501px;width:641px;height:172px;background:var(--blue);color:var(--white)}
  .back__cta{position:absolute;left:52px;top:22px;font-size:33px;line-height:41px}
  .back__contacts{position:absolute;left:52px;top:124px;gap:16px;font-size:12.5px;color:var(--white)}
  .back__contacts svg{stroke:var(--white)}
  .back__brand{left:664px;top:70px;font-size:18px}
  .back__brand .brand__mark{width:18px;height:18px}
  .stamp{left:886px;top:43px;width:84px;height:84px;background:#ededef}
  .address-line{left:663px;width:276px;height:1px;background:#bfc1c8}
</style>
</head>
<body>

<section class="card card--front">
  <div class="abs front__hero"></div>
  <div class="abs front__network" role="img" aria-label="Stylised facility network map with a highlighted blue route"></div>

  <div class="abs brand front__brand"><span class="brand__mark"></span>Quarrytide Hosting</div>
  <h1 class="abs display front__title">Transform Mining<br>With Cohosting</h1>
  <p class="abs front__lede">Miners deserve the best - choose the hosting company that delivers excellence!</p>

  <div class="abs tag" style="left:593px;top:40px"><svg viewBox="0 0 24 24"><path d="M12 3l7 3v6c0 4-3 7-7 9-4-2-7-5-7-9V6z"/><path d="M9 12l2 2 4-4"/></svg>New Secure Facility</div>
  <div class="abs tag" style="left:795px;top:120px"><svg viewBox="0 0 24 24"><path d="M4 17a8 8 0 1 1 16 0z"/><path d="M12 17l4-5"/></svg>Speedy Support</div>
  <div class="abs tag" style="left:551px;top:202px"><svg viewBox="0 0 24 24"><path d="M14 4c3 0 6 0 6 0s0 3 0 6l-8 8-6-6z"/><path d="M7 14l-3 6 6-3"/></svg>99.45% Uptime</div>
  <div class="abs tag" style="left:721px;top:283px"><svg viewBox="0 0 24 24"><path d="M7 18a4 4 0 0 1 0-8 6 6 0 0 1 11 1 3.5 3.5 0 0 1-1 7z"/></svg>24/7 Remote Access</div>

  <div class="abs offer">
    <div class="offer__copy">
      <p>Quarrytide Hosting stands out in the industry by offering both GPU Hosting and ASIC Hosting services in our state-of-the-art facility, equipped with an impressive 17 Megawatts of available power.</p>
      <p>What sets us apart is our unique billing system based on actual metered power usage.</p>
    </div>
    <div class="offer__rates">
      <div class="offer__lead">We charge</div>
      <div class="offer__prices">
        <div class="price"><b>$0.08</b><span>ASIC miners</span></div>
        <div class="price"><b>$0.09</b><span>GPU miners</span></div>
      </div>
    </div>
    <p class="offer__note">ensuring cost-effectiveness and transparency for our clients.</p>
  </div>

  <div class="abs service" style="left:343px">
    <div class="service__icon" role="img" aria-label="GPU card icon"></div>
    <h3 class="service__name">GPU Hosting</h3>
    <p class="service__text">Begin your GPU Hosting journey with rates starting at $0.09 kWh, accepting all equipment.</p>
  </div>
  <div class="abs divider" style="left:465px"></div>
  <div class="abs service" style="left:490px">
    <div class="service__icon" role="img" aria-label="ASIC chip icon"></div>
    <h3 class="service__name">ASIC Hosting</h3>
    <p class="service__text">Get your ASICs directly from us or send yours in today, starting at an all-in rate of $0.08 kWh.</p>
  </div>
  <div class="abs divider" style="left:612px"></div>
  <div class="abs service" style="left:635px">
    <div class="service__icon" role="img" aria-label="Mining fan hardware icon"></div>
    <h3 class="service__name">Mining Hardware</h3>
    <p class="service__text">Looking for mining hardware? Our equipment comes with no additional markup, ever.</p>
  </div>
  <div class="abs divider" style="left:776px"></div>
  <div class="abs service service--wide" style="left:806px">
    <div class="service__icon" role="img" aria-label="Consulting icon"></div>
    <h3 class="service__name">Crypto Consulting</h3>
    <p class="service__text">Enjoy complete White Glove Services for setup, insurance, and tax consulting.</p>
  </div>

  <div class="abs front__bar"></div>
  <div class="abs contacts front__contacts">
    <span><svg viewBox="0 0 24 24"><path d="M5 4h4l2 5-3 2a11 11 0 0 0 5 5l2-3 5 2v4a2 2 0 0 1-2 2A16 16 0 0 1 3 6a2 2 0 0 1 2-2z"/></svg>Schedule 1-On-1</span>
    <span><svg viewBox="0 0 24 24"><rect x="3" y="5" width="18" height="14" rx="1"/><path d="M3 6l9 7 9-7"/></svg>hello@quarrytidehosting.example</span>
    <span><svg viewBox="0 0 24 24"><circle cx="12" cy="12" r="9"/><path d="M3 12h18M12 3c3 3 3 15 0 18M12 3c-3 3-3 15 0 18"/></svg>quarrytidehosting.example</span>
  </div>
</section>

<section class="card card--back">
  <h2 class="abs display back__title">Solutions For Every Miner,<br>Regardless Of Scale</h2>
  <p class="abs back__lede">Our solutions cater to cryptominers of all sizes, providing tailored options to meet diverse operational needs.</p>

  <article class="abs plan plan--gpu">
    <div class="plan__head"><div class="plan__icon" role="img" aria-label="GPU card icon"></div><h3 class="plan__name">GPU<br>Hosting</h3></div>
    <p class="plan__text">Benefit from GPU hosting at an affordable rate of $0.09 per kilowatt-hour, ensuring cost-effective operations for your mining needs on any algorithm.</p>
    <ul class="plan__list">
      <li><svg viewBox="0 0 16 16"><circle cx="8" cy="8" r="7" fill="#c8d1f8"/><path d="M5 8l2 2 4-4" stroke="#3d5af1" stroke-width="1.6" fill="none"/></svg>One Time Setup Fee of $50 Per GPU Rig</li>
      <li><svg viewBox="0 0 16 16"><circle cx="8" cy="8" r="7" fill="#c8d1f8"/><path d="M5 8l2 2 4-4" stroke="#3d5af1" stroke-width="1.6" fill="none"/></svg>All-In $0.09 Per Kilowatt-Hour, No Additional Fees</li>
      <li><svg viewBox="0 0 16 16"><circle cx="8" cy="8" r="7" fill="#c8d1f8"/><path d="M5 8l2 2 4-4" stroke="#3d5af1" stroke-width="1.6" fill="none"/></svg>Remotely Monitor &amp; Access Your Equipment 24/7</li>
    </ul>
  </article>

  <article class="abs plan plan--asic">
    <div class="plan__head"><div class="plan__icon" role="img" aria-label="ASIC chip icon"></div><h3 class="plan__name">ASIC<br>Hosting</h3></div>
    <p class="plan__text">Access ASIC hosting at a competitive rate of $0.08 per kilowatt-hour, ensuring efficient and cost-effective operations for your large scale mining endeavors.</p>
    <ul class="plan__list">
      <li><svg viewBox="0 0 16 16"><path d="M3 8l3 3 7-7" stroke="#1f9d4c" stroke-width="1.8" fill="none"/></svg>One Time Setup Fee of $50 Per ASIC Unit</li>
      <li><svg viewBox="0 0 16 16"><path d="M3 8l3 3 7-7" stroke="#1f9d4c" stroke-width="1.8" fill="none"/></svg>All-In $0.08 Per Kilowatt-Hour, No Additional Fees</li>
      <li><svg viewBox="0 0 16 16"><path d="M3 8l3 3 7-7" stroke="#1f9d4c" stroke-width="1.8" fill="none"/></svg>Remotely Monitor &amp; Access Your Equipment 24/7</li>
    </ul>
  </article>

  <div class="abs back__band">
    <h2 class="display back__cta">Have Questions? Contact Us<br>For Expert Advice</h2>
    <div class="contacts back__contacts">
      <span><svg viewBox="0 0 24 24"><path d="M5 4h4l2 5-3 2a11 11 0 0 0 5 5l2-3 5 2v4a2 2 0 0 1-2 2A16 16 0 0 1 3 6a2 2 0 0 1 2-2z"/></svg>Schedule 1-On-1</span>
      <span><svg viewBox="0 0 24 24"><rect x="3" y="5" width="18" height="14" rx="1"/><path d="M3 6l9 7 9-7"/></svg>hello@quarrytidehosting.example</span>
      <span><svg viewBox="0 0 24 24"><circle cx="12" cy="12" r="9"/><path d="M3 12h18M12 3c3 3 3 15 0 18M12 3c-3 3-3 15 0 18"/></svg>quarrytidehosting.example</span>
    </div>
  </div>

  <div class="abs brand back__brand"><span class="brand__mark"></span>Quarrytide Hosting</div>
  <div class="abs stamp"></div>
  <div class="abs address-line" style="top:221px"></div>
  <div class="abs address-line" style="top:288px"></div>
  <div class="abs address-line" style="top:355px"></div>
</section>

</body>
</html>
```